Brightwell is a company offering Colon Hydrotherapy (or colonics)

Brightwell offers Colon Hydrotherapy using an innovative FDA approved system from the USA. The system is called the TORVA system. The clinic is based in Whangarei, Northland and is the first business of this kind for Northland.
I used to use a design from the Printlane website - a water symbol. However, I want a design that will convey freshness. I want something new and clean which conveys vitality and revitalisation .... perhaps water or bubbles but which brings across the idea of detoxing (which is what colon hydrotherapy does)
The clinic will only be completed in April so for now I have put my mobile number but once in the clinic this will need to be changed to a landline number ... the email address will also change. Thanks for any ideas you give me,
Updates

Hi. I need the name Brightwell first and foremost as this is the name of the Company Underneath this it has to say Colon Hydrotherapy to let people know what Brightwell is My name underneath that would be Miriam Holloway And all contact details to follow this. Thanks !

Target Market(s)

People who are wanting to "detox" and focusing on their health and wellbeing

Industry/Entity Type

Clinic

Contact Information for Business Card

Brightwell
Colon Hydrotherapy
Miriam Holloway
Unit B, 42c Harbour Lane, Whangarei

021 0487 3926
brightwellcare@mailnest.example

Font styles to use
Serif

Colors
cee9f6
33a6d7
86cae6

Requirements
Must have
• Stand out with colour or logo

```html
<!DOCTYPE html>
<html lang="en">
<head>
<meta charset="utf-8">
<title>Brightwell Colon Hydrotherapy – Business Cards</title>
<link rel="stylesheet" href="https://fonts.googleapis.com/css2?family=Source+Serif+4:wght@400;600;700&display=swap">
<style>
  :root {
    --page-bg: #e9eef1;
    --card-deep: #0b4f8a;
    --card-mid: #1466a8;
    --card-light: #2b86c4;
    --glow: rgba(134, 202, 230, 0.22);
    --accent-green: #b5d334;
    --sky: #86cae6;
    --ice: #cee9f6;
    --white: #ffffff;
  }
  html, body {
    margin: 0;
    width: 1200px;
    height: 1023px;
    overflow: hidden;
    background: var(--page-bg);
    font-family: "Source Serif 4", Georgia, serif;
  }
  .stage {
    position: relative;
    width: 1200px;
    height: 1023px;
  }
  .card {
    position: absolute;
    width: 560px;
    height: 340px;
    border-radius: 22px;
    overflow: hidden;
    box-shadow: 0 14px 30px rgba(10, 40, 70, 0.28);
  }
  .card-front {
    left: 90px;
    top: 110px;
    background: linear-gradient(200deg, var(--card-deep) 0%, var(--card-mid) 45%, var(--card-light) 75%, var(--card-mid) 100%);
  }
  .card-back {
    left: 550px;
    top: 570px;
    background: linear-gradient(160deg, var(--card-mid) 0%, var(--card-deep) 100%);
  }
  .corner-glow {
    position: absolute;
    right: 0;
    top: 0;
    width: 320px;
    height: 200px;
    background: radial-gradient(ellipse at 100% 0%, var(--glow) 0%, rgba(134,202,230,0.08) 55%, rgba(134,202,230,0) 75%);
  }
  .front-content {
    position: absolute;
    left: 40px;
    bottom: 28px;
    color: var(--white);
  }
  .brand {
    display: flex;
    align-items: center;
    gap: 10px;
  }
  .brand-dot {
    width: 20px;
    height: 20px;
    border-radius: 50%;
    background: var(--accent-green);
  }
  .brand-name {
    font-size: 40px;
    font-weight: 600;
    color: var(--white);
    line-height: 1;
  }
  .brand-tagline {
    font-size: 19px;
    color: var(--sky);
    margin: 6px 0 0 30px;
  }
  .person {
    margin: 14px 0 0 30px;
  }
  .person-name {
    font-size: 22px;
    font-weight: 700;
    color: var(--accent-green);
    letter-spacing: 0.3px;
  }
  .person-role {
    font-size: 13px;
    color: var(--white);
    margin-top: 2px;
  }
  .contact {
    margin: 10px 0 0 30px;
    font-size: 14px;
    line-height: 24px;
  }
  .contact-row {
    display: flex;
    align-items: center;
    gap: 8px;
  }
  .contact-icon {
    width: 16px;
    height: 16px;
    border-radius: 3px;
    background: var(--accent-green);
    display: inline-flex;
    align-items: center;
    justify-content: center;
  }
  .address {
    margin-top: 6px;
    font-size: 14px;
    font-weight: 700;
    color: var(--accent-green);
    text-transform: uppercase;
  }
  .back-oval {
    position: absolute;
    left: 60px;
    top: 40px;
    width: 440px;
    height: 260px;
    border-radius: 50%;
    background: radial-gradient(ellipse at center, rgba(134,202,230,0.18) 0%, rgba(134,202,230,0.08) 60%, rgba(134,202,230,0) 75%);
  }
  .back-content {
    position: absolute;
    inset: 0;
    display: flex;
    flex-direction: column;
    align-items: center;
    justify-content: center;
    color: var(--white);
  }
  .back-content .brand-name {
    font-size: 56px;
  }
  .back-content .brand-tagline {
    color: var(--ice);
    font-size: 26px;
    margin: 8px 0 0;
  }
</style>
</head>
<body>
<main class="stage">

  <section class="card card-front">
    <div class="corner-glow" role="img" aria-label="Soft light blue water ripple decoration in the corner"></div>
    <div class="front-content">
      <div class="brand">
        <span class="brand-dot"></span>
        <span class="brand-name">Brightwell</span>
      </div>
      <div class="brand-tagline">Colon Hydrotherapy</div>
      <div class="person">
        <div class="person-name">Miriam Holloway</div>
        <div class="person-role">Project Manager</div>
      </div>
      <div class="contact">
        <div class="contact-row">
          <span class="contact-icon">
            <svg width="10" height="10" viewBox="0 0 10 10" aria-hidden="true"><path d="M2 1 L4 1 L4.6 3 L3.5 3.8 Q4.5 5.8 6.2 6.5 L7 5.4 L9 6 L9 8 Q5 9 2 5 Q1 3 2 1Z" fill="var(--card-deep)"/></svg>
          </span>
          021 0487 3926
        </div>
        <div class="contact-row">
          <span class="contact-icon">
            <svg width="10" height="10" viewBox="0 0 10 10" aria-hidden="true"><rect x="1" y="2.5" width="8" height="5.5" fill="none" stroke="var(--card-deep)" stroke-width="1.2"/><path d="M1 2.5 L5 5.5 L9 2.5" fill="none" stroke="var(--card-deep)" stroke-width="1.2"/></svg>
          </span>
          brightwellcare@mailnest.example
        </div>
        <div class="address">Unit B, 42c Harbour Lane, Whangarei</div>
      </div>
    </div>
  </section>

  <section class="card card-back">
    <div class="back-oval" role="img" aria-label="Soft light oval glow behind the company name"></div>
    <div class="back-content">
      <div class="brand-name">Brightwell</div>
      <div class="brand-tagline">Colon Hydrotherapy</div>
    </div>
  </section>

</main>
</body>
</html>
```